TOPページのイメージを作成していただきたいです。
女性が入りやすく、親しみやすい色使いとフォントで、
カテゴリのボタンはアイコン等を使い、やわらかい印象を与えたい
※アイコンを指定しているわけではありません。

商品にカラフルなものが多くなりやすいので、全体的な色バランスはシンプルなカラーでお願いします。
サイドバナーとメインに上記スクールをターゲットとしたカテゴリに飛ぶためのバナー用意してほしいです。
近いサイトイメージは合わせて送らせていただきます。
スマートフォンでも表示させやすいレイアウトを希望します。
Quelvoのショッピングに関しては、Quelvoプリズマを契約予定です。
また、今回はトップページだけですが、契約させて頂いた方には商品ページなどサブページも依頼する可能性が高いです

-------------------
項目について
-------------------
※スプレッドシート参照
https://sheets.tavrolink.com/spreadsheets/d/7pxQwLzNc4bTr2VhYk9MeJsA8uDfGiHo3nKyRtE5WqPl/edit?usp=sharing
■ヘッダー
検索窓、お支払いについて、送料、お届けについて、返品、交換、保証について、会社概要、プライバシーポリシー、お問い合わせ、よくある質問
■フッター
店舗内簡易情報として、イメージ画像のような下記の内容を用意する予定で、記述箇所のデザインを用意してください
送料について、支払い方法について、手数料、納期、キャンセルについて、商品の在庫について
■カテゴリ
カテゴリは、別紙の資料の通りです。
大カテゴリがメイン、中に小カテゴリがあります。

■写真資料
https://files.tavrolink.com/file/d/9kd3RwQ7mZ2xVbN8pLcT4yHsJfGeAu6Wn/view?usp=sharing

■サイト見本イメージ
https://store.mirubeta.jp/pastelnook/
https://yarn-lumio.com/
https://ec.stitchvale.jp/
https://www.tomiseki.co.jp/shop/c/c10/
https://www.webshop.mirel-kasano.com/
https://works.brevok.net/
サイトの色合いや雰囲気に近いサイトになります。
1ページ
赤系、黄・オレンジ系、茶系
• イラストレーター形式 (.ai)
幅1250px程度
※Quelvoショップのバナーサイズを考慮しています。
場合によってはその他のページもお願いする可能性があります。
もう少し提案数を頂きたいため、5月13日(金)までコンペの延長をいたします。

今回選ばせていただきました理由は
・商品を邪魔しないシンプルさ
・Quelvoショップに落とし込んだ時に差異が生まれにくい点
・全体的な色使い
を中心に選ばせていただきました。
非常にあたたかく、親しみやすいデザインで作成いただきましたので、こちらに決定させていただきました。

今回いただきました提案はどれも素晴らしく、選考は非常に悩みました。
冒険するか、無難なデザインにするか、また、その中でもどれがいいか、かなり悩みまして、選ばれなかったデザインも、最後までの残ったデザインがいくつかございました。
本当に皆様ご提案ありがとうございました。
また次の機会がございましたら、是非よろしくお願いします。

```html
<!DOCTYPE html>
<html lang="ja">
<head>
<meta charset="utf-8">
<title>ハンドメイド shop もくれん</title>
<link href="https://fonts.googleapis.com/css2?family=M+PLUS+Rounded+1c:wght@400;500;700;800&family=Zen+Maru+Gothic:wght@500;700&display=swap" rel="stylesheet">
<style>
:root{
  --red:#d8263e;
  --red-dark:#b81c31;
  --beige:#d3b894;
  --beige-light:#efe4d3;
  --beige-pale:#f7f1e8;
  --text:#3b3330;
  --muted:#8a7d72;
  --line:#e6ddd2;
  --grey:#f0efed;
  --white:#ffffff;
}
*{margin:0;padding:0;box-sizing:border-box}
html,body{width:1200px;height:3936px;overflow:hidden;background:var(--white)}
body{position:relative;font-family:"M PLUS Rounded 1c",sans-serif;color:var(--text);font-size:13px}
.abs{position:absolute}

/* header */
.site-header{top:0;left:0;width:1200px;height:120px}
.brand{left:60px;top:26px}
.brand-sub{font-size:11px;color:var(--muted);letter-spacing:.1em}
.brand-name{font-family:"Zen Maru Gothic",sans-serif;font-weight:700;font-size:40px;color:var(--red);line-height:1.1}
.search{left:330px;top:44px;width:540px;height:38px;border:1px solid var(--line);border-radius:4px;display:flex;align-items:center;padding:0 14px;color:#b5aaa0;font-size:13px;justify-content:space-between}
.top-nav{right:56px;top:18px;font-size:11px;color:var(--muted);display:flex;gap:12px}
.icon-nav{right:56px;top:44px;display:flex;gap:26px}
.icon-nav div{display:flex;flex-direction:column;align-items:center;font-size:10px;color:var(--muted);gap:3px}

/* notice */
.notice{top:124px;left:0;width:1200px;height:36px;background:var(--red);color:var(--white);font-weight:700;font-size:15px;display:flex;align-items:center;justify-content:center;letter-spacing:.04em}

/* hero */
.hero{top:160px;left:0;width:1200px;height:410px;overflow:hidden}
.hero-side{top:10px;height:390px;width:220px}
.hero-left{left:0;background:linear-gradient(135deg,#2b2b2b,#6b5b50 60%,#c8c2b8)}
.hero-right{right:0;background:linear-gradient(135deg,#f3f1ee,#c9d6e8 50%,#6f8fc4)}
.hero-main{left:240px;top:10px;width:720px;height:390px;background:linear-gradient(120deg,#d9c8b0,#eadfcf 45%,#b7a892);}
.hero-copy{right:60px;top:70px;text-align:center}
.hero-copy .small{font-family:"Zen Maru Gothic",sans-serif;font-size:20px;color:var(--white);font-weight:700}
.hero-copy .big{font-family:"Zen Maru Gothic",sans-serif;font-size:52px;font-weight:700;color:#e8566b;line-height:1.2}
.hero-copy .sub{font-family:"Zen Maru Gothic",sans-serif;font-size:30px;color:var(--white);font-weight:700}
.dots{top:586px;left:0;width:1200px;display:flex;justify-content:center;gap:10px}
.dots span{width:9px;height:9px;border-radius:50%;background:var(--line)}
.dots span.on{background:var(--red)}

.divider{left:0;width:1200px;height:10px}

/* sidebar */
.sidebar{left:60px;top:720px;width:240px}
.cat-list{list-style:none;border-top:1px solid var(--line)}
.cat-list li{height:44px;display:flex;align-items:center;gap:10px;padding-left:8px;border-bottom:1px solid var(--line);font-size:13px;font-weight:500;white-space:nowrap}
.cat-list li.on{background:var(--beige-pale);color:var(--red)}
.cat-ico{width:22px;height:22px;border-radius:50%;background:var(--beige-light);display:flex;align-items:center;justify-content:center}
.flyout{left:300px;top:764px;width:176px;z-index:5;background:var(--white);border:1px solid var(--line);box-shadow:0 2px 6px rgba(0,0,0,.08)}
.flyout div{height:40px;display:flex;align-items:center;padding-left:14px;font-size:12px;white-space:nowrap;border-bottom:1px solid var(--line)}
.flyout div:last-child{border-bottom:none}
.flyout div.on{background:var(--beige-pale);color:var(--red)}
.side-banner{left:60px;top:1330px;width:240px;height:100px;background:linear-gradient(135deg,#cbb9a3,#e9dfd2);border-radius:4px}

/* main */
.section{left:500px;width:660px}
.sec-head{text-align:center;height:110px}
.sec-head svg{display:block;margin:0 auto 6px}
.sec-title{font-size:24px;font-weight:800;letter-spacing:.06em}
.sec-sub{font-size:10px;color:var(--beige);letter-spacing:.2em;margin-top:2px}
.cards{display:flex;justify-content:center;gap:30px}
.card{width:200px;position:relative}
.card .photo{width:200px;height:200px;border-radius:2px}
.card .name{font-size:12px;margin:10px 0 6px;white-space:nowrap}
.price{background:var(--beige-light);text-align:center;font-size:13px;font-weight:700;color:var(--red);height:26px;line-height:26px;border-radius:13px;white-space:nowrap}
.heart{position:absolute;right:8px;top:8px}
.tag-new{position:absolute;left:0;top:0;background:var(--red);color:var(--white);font-size:10px;font-weight:700;padding:3px 8px}
.medal{position:absolute;left:50%;top:182px;transform:translateX(-50%);width:36px;height:36px;border-radius:50%;color:var(--white);font-weight:800;font-size:15px;display:flex;align-items:center;justify-content:center;border:3px solid var(--white)}
.more{margin:34px auto 0;width:160px;height:40px;border-radius:20px;background:var(--beige);color:var(--white);font-size:13px;font-weight:700;display:flex;align-items:center;justify-content:center}
.cards.four{gap:20px}
.cards.four .card{width:150px}
.cards.four .photo{width:150px;height:150px}
.cards.four .price{font-size:12px}

.tabs{display:flex;justify-content:center;gap:16px;margin-bottom:20px}
.tab{width:200px;height:34px;display:flex;align-items:center;justify-content:center;font-weight:700;font-size:13px;border:1px solid var(--red);color:var(--red)}
.tab.on{background:var(--red);color:var(--white)}
.banners{display:grid;grid-template-columns:320px 320px;gap:20px;justify-content:center}
.banner{height:140px;background:var(--grey);display:flex;align-items:center;justify-content:center;font-size:22px;font-weight:700;color:#555}

.guides{display:flex;justify-content:center;gap:20px}
.guide{width:150px}
.guide .photo{width:150px;height:150px}
.guide p{font-size:12px;margin-top:10px;line-height:1.5}

/* footer */
.site-footer{top:3780px;left:0;width:1200px;height:156px;background:var(--red);color:var(--white)}
.foot-brand{left:60px;top:36px}
.foot-brand .brand-sub{color:#f7d3d8}
.foot-brand .brand-name{color:var(--white)}
.foot-links{left:360px;top:58px;display:flex;gap:18px;font-size:13px;white-space:nowrap}
.copy{left:0;top:124px;width:1200px;text-align:center;font-size:10px;color:#f7d3d8}
</style>
</head>
<body>

<header class="site-header abs">
  <div class="brand abs"><div class="brand-sub">ハンドメイド shop</div><div class="brand-name">もくれん</div></div>
  <div class="search abs"><span>商品名・キーワード</span>
    <svg width="16" height="16" viewBox="0 0 16 16"><circle cx="7" cy="7" r="5" fill="none" stroke="#3b3330" stroke-width="2"/><path d="M11 11l4 4" stroke="#3b3330" stroke-width="2"/></svg></div>
  <nav class="top-nav abs"><span>お支払いについて</span><span>送料・お届けについて</span><span>返品・交換・保証について</span><span>会社概要</span><span>プライバシーポリシー</span><span>お問い合わせ</span><span>よくある質問</span></nav>
  <div class="icon-nav abs">
    <div><svg width="26" height="24" viewBox="0 0 26 24"><path d="M13 22S2 14.5 2 8a5.5 5.5 0 0 1 11-1 5.5 5.5 0 0 1 11 1c0 6.5-11 14-11 14z" fill="none" stroke="#3b3330" stroke-width="2"/></svg>お気に入り</div>
    <div><svg width="26" height="24" viewBox="0 0 26 24"><path d="M1 2h4l3 13h13l3-9H7" fill="none" stroke="#3b3330" stroke-width="2"/><circle cx="10" cy="20" r="2" fill="#3b3330"/><circle cx="19" cy="20" r="2" fill="#3b3330"/></svg>カート</div>
    <div><svg width="26" height="24" viewBox="0 0 26 24"><circle cx="13" cy="7" r="5" fill="none" stroke="#3b3330" stroke-width="2"/><path d="M3 23c1-6 5-8 10-8s9 2 10 8" fill="none" stroke="#3b3330" stroke-width="2"/></svg>マイページ</div>
  </div>
</header>

<div class="notice abs">新規ご登録のお客様、送料無料キャンペーン中！</div>

<section class="hero abs">
  <div class="hero-side hero-left abs" role="img" aria-label="黒いバッグと小物の写真"></div>
  <div class="hero-main abs" role="img" aria-label="テーブルで工作をする子どもの写真">
    <div class="hero-copy abs"><div class="small">お子様と楽しめる</div><div class="big">ワークショップ</div><div class="sub">商品充実♪</div></div>
  </div>
  <div class="hero-side hero-right abs" role="img" aria-label="青い花柄のシート素材の写真"></div>
</section>
<div class="dots abs"><span class="on"></span><span></span><span></span><span></span></div>

<svg class="divider abs" style="top:655px" viewBox="0 0 1200 10"><path d="M40 5 H1160" stroke="#d3b894" stroke-width="2" stroke-dasharray="6 6"/></svg>

<aside class="sidebar abs">
  <ul class="cat-list">
    <li><span class="cat-ico"><svg width="12" height="12"><rect x="1" y="2" width="10" height="8" fill="#d3b894"/></svg></span>布地商品</li>
    <li class="on"><span class="cat-ico"><svg width="12" height="12"><circle cx="6" cy="6" r="4" fill="#d8263e"/></svg></span>塗料・ペイント・プリント</li>
    <li><span class="cat-ico"><svg width="12" height="12"><rect x="2" y="2" width="8" height="8" fill="#d3b894"/></svg></span>加工素材</li>
    <li><span class="cat-ico"><svg width="12" height="12"><path d="M2 10L10 2" stroke="#d3b894" stroke-width="2"/></svg></span>刺繍商品</li>
    <li><span class="cat-ico"><svg width="12" height="12"><path d="M3 3l6 6M9 3l-6 6" stroke="#d3b894" stroke-width="2"/></svg></span>加工道具</li>
    <li><span class="cat-ico"><svg width="12" height="12"><rect x="1" y="4" width="10" height="7" fill="#d3b894"/></svg></span>キット商品</li>
    <li><span class="cat-ico"><svg width="12" height="12"><path d="M2 5h8v6H2z" fill="#d3b894"/></svg></span>袋小物</li>
    <li><span class="cat-ico"><svg width="12" height="12"><path d="M6 1l5 10H1z" fill="#d3b894"/></svg></span>雑貨</li>
    <li><span class="cat-ico"><svg width="12" height="12"><circle cx="6" cy="6" r="4" fill="#d3b894"/></svg></span>ワックス商品</li>
    <li><span class="cat-ico"><svg width="12" height="12"><path d="M2 4h8l-1 7H3z" fill="#d3b894"/></svg></span>バッグ商品</li>
    <li><span class="cat-ico"><svg width="12" height="12"><rect x="2" y="3" width="8" height="6" fill="#d3b894"/></svg></span>アイロンシート・転写紙</li>
    <li><span class="cat-ico"><svg width="12" height="12"><rect x="1" y="3" width="10" height="6" fill="#d3b894"/></svg></span>プリントキット</li>
    <li><span class="cat-ico"><svg width="12" height="12"><path d="M6 1l1.5 3.5L11 5l-2.5 2.5.6 3.5L6 9.3 2.9 11l.6-3.5L1 5l3.5-.5z" fill="#d3b894"/></svg></span>スタートキット</li>
  </ul>
</aside>
<div class="flyout abs"><div>アクリル絵具</div><div class="on">布用絵具・ペン</div><div>ネットシルク商品</div></div>
<div class="side-banner abs" role="img" aria-label="スクール向けカテゴリへのバナー写真"></div>

<section class="section abs" style="top:720px">
  <div class="sec-head"><svg width="34" height="34" viewBox="0 0 34 34"><rect x="5" y="13" width="24" height="18" fill="none" stroke="#d3b894" stroke-width="2"/><rect x="3" y="8" width="28" height="6" fill="none" stroke="#d3b894" stroke-width="2"/><path d="M17 8v23" stroke="#d3b894" stroke-width="2"/></svg>
    <div class="sec-title">おすすめアイテム</div><div class="sec-sub">RECOMMEND</div></div>
  <div class="cards">
    <div class="card"><div class="photo" style="background:linear-gradient(160deg,#fff,#eee5d6)" role="img" aria-label="帆布トートバッグの商品写真"></div><svg class="heart" width="22" height="20" viewBox="0 0 26 24"><path d="M13 22S2 14.5 2 8a5.5 5.5 0 0 1 11-1 5.5 5.5 0 0 1 11 1c0 6.5-11 14-11 14z" fill="none" stroke="#8a7d72" stroke-width="2"/></svg><div class="name">帆布トートバッグ</div><div class="price">1,100 円（税込）</div></div>
    <div class="card"><div class="photo" style="background:linear-gradient(160deg,#fff,#f4ecd8)" role="img" aria-label="黄色いナイフの商品写真"></div><svg class="heart" width="22" height="20" viewBox="0 0 26 24"><path d="M13 22S2 14.5 2 8a5.5 5.5 0 0 1 11-1 5.5 5.5 0 0 1 11 1c0 6.5-11 14-11 14z" fill="none" stroke="#8a7d72" stroke-width="2"/></svg><div class="name">ナイフ</div><div class="price">858 円（税込）</div></div>
    <div class="card"><div class="photo" style="background:linear-gradient(160deg,#f2f2f2,#c9c9c9)" role="img" aria-label="白い布の商品写真"></div><span class="tag-new">NEW!</span><svg class="heart" width="22" height="20" viewBox="0 0 26 24"><path d="M13 22S2 14.5 2 8a5.5 5.5 0 0 1 11-1 5.5 5.5 0 0 1 11 1c0 6.5-11 14-11 14z" fill="none" stroke="#8a7d72" stroke-width="2"/></svg><div class="name">布（白）</div><div class="price">1,100 円（税込）</div></div>
  </div>
  <div class="more">もっと見る</div>
</section>
<svg class="divider abs" style="top:1235px" viewBox="0 0 1200 10"><path d="M500 5 H1160" stroke="#d3b894" stroke-width="2" stroke-dasharray="6 6"/></svg>

<section class="section abs" style="top:1270px">
  <div class="sec-head"><svg width="36" height="30" viewBox="0 0 36 30"><path d="M3 26L5 8l8 8 5-12 5 12 8-8 2 18z" fill="#d3b894"/></svg>
    <div class="sec-title">人気ランキング</div><div class="sec-sub">RANKING</div></div>
  <div class="cards">
    <div class="card"><div class="photo" style="background:linear-gradient(160deg,#6b4a2e,#e6ddd2 60%,#fff)" role="img" aria-label="プロッターの商品写真"></div><span class="medal" style="background:#d4a92c">1</span><svg class="heart" width="22" height="20" viewBox="0 0 26 24"><path d="M13 22S2 14.5 2 8a5.5 5.5 0 0 1 11-1 5.5 5.5 0 0 1 11 1c0 6.5-11 14-11 14z" fill="none" stroke="#fff" stroke-width="2"/></svg><div class="name" style="margin-top:24px">プロッター</div><div class="price">6,880 円（税込）</div></div>
    <div class="card"><div class="photo" style="background:linear-gradient(160deg,#fff,#f4ecd8)" role="img" aria-label="黄色いナイフの商品写真"></div><span class="medal" style="background:#a9a9ad">2</span><svg class="heart" width="22" height="20" viewBox="0 0 26 24"><path d="M13 22S2 14.5 2 8a5.5 5.5 0 0 1 11-1 5.5 5.5 0 0 1 11 1c0 6.5-11 14-11 14z" fill="none" stroke="#8a7d72" stroke-width="2"/></svg><div class="name" style="margin-top:24px">ナイフ</div><div class="price">858 円（税込）</div></div>
    <div class="card"><div class="photo" style="background:linear-gradient(160deg,#1e1e1e,#5a5a5a 50%,#e8e8e8)" role="img" aria-label="白黒のシートの商品写真"></div><span class="medal" style="background:#b87a48">3</span><svg class="heart" width="22" height="20" viewBox="0 0 26 24"><path d="M13 22S2 14.5 2 8a5.5 5.5 0 0 1 11-1 5.5 5.5 0 0 1 11 1c0 6.5-11 14-11 14z" fill="none" stroke="#fff" stroke-width="2"/></svg><div class="name" style="margin-top:24px">シート</div><div class="price">1,100 円（税込）</div></div>
  </div>
  <div class="more">もっと見る</div>
</section>
<svg class="divider abs" style="top:1785px" viewBox="0 0 1200 10"><path d="M500 5 H1160" stroke="#d3b894" stroke-width="2" stroke-dasharray="6 6"/></svg>

<section class="section abs" style="top:1820px">
  <div class="sec-head"><svg width="34" height="34" viewBox="0 0 34 34"><path d="M17 2l4.5 9.5L32 13l-7.5 7 2 10.5L17 25.5 7.5 30.5l2-10.5L2 13l10.5-1.5z" fill="none" stroke="#d3b894" stroke-width="2"/></svg>
    <div class="sec-title">新着アイテム</div><div class="sec-sub">NEW ARRIVAL</div></div>
  <div class="cards">
    <div class="card"><div class="photo" style="background:linear-gradient(160deg,#fff,#e8eef5 50%,#f5d9dc)" role="img" aria-label="カラフルなワッペンの商品写真"></div><span class="tag-new">NEW!</span><svg class="heart" width="22" height="20" viewBox="0 0 26 24"><path d="M13 22S2 14.5 2 8a5.5 5.5 0 0 1 11-1 5.5 5.5 0 0 1 11 1c0 6.5-11 14-11 14z" fill="none" stroke="#8a7d72" stroke-width="2"/></svg><div class="name">クラフトバッジ</div><div class="price">1,680 円（税込）</div></div>
    <div class="card"><div class="photo" style="background:linear-gradient(160deg,#fff,#eee5d6)" role="img" aria-label="帆布トートバッグの商品写真"></div><span class="tag-new">NEW!</span><svg class="heart" width="22" height="20" viewBox="0 0 26 24"><path d="M13 22S2 14.5 2 8a5.5 5.5 0 0 1 11-1 5.5 5.5 0 0 1 11 1c0 6.5-11 14-11 14z" fill="none" stroke="#8a7d72" stroke-width="2"/></svg><div class="name">帆布トートバッグ</div><div class="price">1,100 円（税込）</div></div>
    <div class="card"><div class="photo" style="background:linear-gradient(160deg,#1e1e1e,#5a5a5a 50%,#e8e8e8)" role="img" aria-label="白黒のシートの商品写真"></div><span class="tag-new">NEW!</span><svg class="heart" width="22" height="20" viewBox="0 0 26 24"><path d="M13 22S2 14.5 2 8a5.5 5.5 0 0 1 11-1 5.5 5.5 0 0 1 11 1c0 6.5-11 14-11 14z" fill="none" stroke="#fff" stroke-width="2"/></svg><div class="name">シート</div><div class="price">1,100 円（税込）</div></div>
  </div>
  <div class="more">もっと見る</div>
</section>
<svg class="divider abs" style="top:2320px" viewBox="0 0 1200 10"><path d="M500 5 H1160" stroke="#d3b894" stroke-width="2" stroke-dasharray="6 6"/></svg>

<section class="section abs" style="top:2355px">
  <div class="sec-head"><svg width="34" height="34" viewBox="0 0 34 34"><path d="M4 4h13l14 14-13 13L4 17z" fill="none" stroke="#d3b894" stroke-width="2"/><circle cx="11" cy="11" r="2.5" fill="#d3b894"/></svg>
    <div class="sec-title">セール品</div><div class="sec-sub">SALE</div></div>
  <div class="cards four">
    <div class="card"><div class="photo" style="background:linear-gradient(160deg,#fff,#f0d5d8)" role="img" aria-label="転写シールの商品写真"></div><svg class="heart" width="20" height="18" viewBox="0 0 26 24"><path d="M13 22S2 14.5 2 8a5.5 5.5 0 0 1 11-1 5.5 5.5 0 0 1 11 1c0 6.5-11 14-11 14z" fill="none" stroke="#8a7d72" stroke-width="2"/></svg><div class="name">転写シール</div><div class="price">2,200 円（税込）</div></div>
    <div class="card"><div class="photo" style="background:linear-gradient(160deg,#fff,#e7ecf3 50%,#f3d7cf)" role="img" aria-label="刺繍ペンの商品写真"></div><svg class="heart" width="20" height="18" viewBox="0 0 26 24"><path d="M13 22S2 14.5 2 8a5.5 5.5 0 0 1 11-1 5.5 5.5 0 0 1 11 1c0 6.5-11 14-11 14z" fill="none" stroke="#8a7d72" stroke-width="2"/></svg><div class="name">刺繍ペン</div><div class="price">3,583 円（税込）</div></div>
    <div class="card"><div class="photo" style="background:linear-gradient(160deg,#fff,#e6e6e6)" role="img" aria-label="プロッターの商品写真"></div><svg class="heart" width="20" height="18" viewBox="0 0 26 24"><path d="M13 22S2 14.5 2 8a5.5 5.5 0 0 1 11-1 5.5 5.5 0 0 1 11 1c0 6.5-11 14-11 14z" fill="none" stroke="#8a7d72" stroke-width="2"/></svg><div class="name">プロッター</div><div class="price">4,500 円（税込）</div></div>
    <div class="card"><div class="photo" style="background:linear-gradient(160deg,#4a3a33,#c98a6a 50%,#e8d9c5)" role="img" aria-label="グリッターの商品写真"></div><svg class="heart" width="20" height="18" viewBox="0 0 26 24"><path d="M13 22S2 14.5 2 8a5.5 5.5 0 0 1 11-1 5.5 5.5 0 0 1 11 1c0 6.5-11 14-11 14z" fill="none" stroke="#fff" stroke-width="2"/></svg><div class="name">グリッター</div><div class="price">3,880 円（税込）</div></div>
  </div>
</section>

<section class="section abs" style="top:2820px">
  <div class="sec-head"><svg width="34" height="34" viewBox="0 0 34 34"><path d="M17 3l3.5 9H30l-7.5 6 3 10L17 22l-8.5 6 3-10L4 12h9.5z" fill="#d3b894"/></svg>
    <div class="sec-title">ピックアップ商品</div><div class="sec-sub">PICK UP</div></div>
  <div class="tabs"><div class="tab on">イベントキット</div><div class="tab">スタートキット</div></div>
  <div class="banners"><div class="banner">バナー</div><div class="banner">バナー</div><div class="banner">バナー</div></div>
</section>

<section class="section abs" style="top:3370px">
  <div class="sec-head"><svg width="34" height="34" viewBox="0 0 34 34"><path d="M5 6h10a3 3 0 0 1 2 1 3 3 0 0 1 2-1h10v22H19a3 3 0 0 0-2 1 3 3 0 0 0-2-1H5z" fill="none" stroke="#d3b894" stroke-width="2"/></svg>
    <div class="sec-title">お役立ちコンテンツ</div><div class="sec-sub">CONTENTS</div></div>
  <div class="guides">
    <div class="guide"><div class="photo" style="background:linear-gradient(160deg,#e04a3a,#f2a65a 50%,#6a8fc0)" role="img" aria-label="カラフルなシート作品の写真"></div><p>シートのカット方法について</p></div>
    <div class="guide"><div class="photo" style="background:linear-gradient(160deg,#f3f0ea,#c9b9a6)" role="img" aria-label="プリントしたシャツの写真"></div><p>シートを使った作品の作り方</p></div>
    <div class="guide"><div class="photo" style="background:linear-gradient(160deg,#2f6fb0,#f0c64a 50%,#e0533f)" role="img" aria-label="絵の具で描いた作品の写真"></div><p>子どもと楽しむペイント入門</p></div>
    <div class="guide"><div class="photo" style="background:linear-gradient(160deg,#ffffff,#9fb8e0 60%,#3d63b3)" role="img" aria-label="青い花柄の素材の写真"></div><p>加工素材の選び方</p></div>
  </div>
</section>

<footer class="site-footer abs">
  <div class="foot-brand abs"><div class="brand-sub">ハンドメイド shop</div><div class="brand-name">もくれん</div></div>
  <nav class="foot-links abs"><span>送料について</span><span>｜</span><span>手数料</span><span>｜</span><span>支払い方法について</span><span>｜</span><span>納期・キャンセルについて</span><span>｜</span><span>商品の在庫について</span><span>｜</span><span>手数料</span></nav>
  <div class="copy abs">Copyright 2022 ハンドメイド shop もくれん All Rights Reserved.</div>
</footer>

</body>
</html>
```